Amber Hollow Productions

I need a business card design for a new freelance film production company using or incorporating the logo:
I want the card to be creative, minimal, yet professional. Feel free to use a variety of different shapes and sizes/ textures for the card.

Industry/Entity Type

Film Production

```html
<!DOCTYPE html>
<html lang="en">
<head>
<meta charset="utf-8">
<title>Amber Hollow Productions — Business Card</title>
<link rel="stylesheet" href="https://fonts.googleapis.com/css2?family=Questrial&display=swap">
<style>
  :root {
    --brand-blue: #0b55a5;
    --rule-black: #000000;
    --paper: #ffffff;
    --text-light: #ffffff;
  }
  html, body {
    margin: 0;
    padding: 0;
    width: 1200px;
    height: 720px;
    overflow: hidden;
    background: var(--paper);
  }
  .card {
    position: relative;
    width: 1200px;
    height: 720px;
    background: var(--paper);
    font-family: "Questrial", "Century Gothic", sans-serif;
    overflow: hidden;
  }
  .block {
    position: absolute;
    background: var(--brand-blue);
  }
  .block--top { left: 608px; top: 0; width: 416px; height: 221px; }
  .block--name { left: 609px; top: 228px; width: 417px; height: 492px; }
  .strip { left: 1070px; top: 0; width: 130px; height: 720px; }
  .rule-vertical {
    position: absolute;
    left: 1047px; top: 0;
    width: 9px; height: 720px;
    background: var(--rule-black);
  }
  .holder-name {
    position: absolute;
    left: 690px; top: 300px;
    margin: 0;
    color: var(--text-light);
    font-size: 43px;
    font-weight: 400;
    letter-spacing: 0.5px;
  }
  .brand-name {
    position: absolute;
    left: 100px; top: 300px;
    width: 470px;
    margin: 0;
    text-align: center;
    color: var(--brand-blue);
    font-size: 46px;
    font-weight: 400;
    line-height: 1.15;
  }
  .base-bar {
    position: absolute;
    left: 0; top: 624px;
    width: 609px; height: 21px;
    background: var(--brand-blue);
  }
  .company-tab {
    position: absolute;
    left: 96px; top: 570px;
    height: 55px;
    padding: 0 26px;
    background: var(--brand-blue);
    border-radius: 11px 11px 0 0;
    color: var(--text-light);
    font-size: 37px;
    line-height: 55px;
    white-space: nowrap;
  }
</style>
</head>
<body>
  <main class="card">
    <p class="brand-name">Amber Hollow<br>Productions</p>

    <div class="company-tab">Amber Hollow Production</div>
    <div class="base-bar"></div>

    <div class="block block--top"></div>
    <div class="block block--name"></div>
    <h1 class="holder-name">Your Name</h1>

    <div class="rule-vertical"></div>
    <div class="block strip"></div>
  </main>
</body>
</html>
```